Business Card - The Harborline Group

We need a business card for a new venture capital fund and innovation accelerator based in San Francisco, CA. The Harborline Group will back, fund and scale life-transforming businesses. We intend to provide capital along with strategic and tactical direction to teams running exponential organizations. We are backing great ideas for vast markets with passionate visionaries. We facilitate the rapid creation of life-transforming businesses, help invent or re-invent critical industries and move the frontier of progress for the good of humankind. Maplecrest University defines Exponential Organizations as those whose impact (cost reduction or output) is disproportionally large – at least 10x larger – compared to its peers because of the use of new organizational techniques that leverage accelerating technologies. ExOs are characterized by a massive transformative purpose (MTP), a skunkworks organization and passionate teams of brilliant mountain-climbers with technical backgrounds.

Industry/Entity Type

Business

Contact Information for Business Card

Peter Odell
Managing Director

peter@theharborlinegroup.com
+1.628.307.4190

Font styles to use
Sans Serif

Requirements
Must have
• - logo
• - website: www.theharborlinegroup.com

```html
<!DOCTYPE html>
<html lang="en">
<head>
<meta charset="utf-8">
<title>The Harborline Group – Business Card</title>
<link href="https://fonts.googleapis.com/css2?family=Open+Sans:wght@400;600;700&display=swap" rel="stylesheet">
<style>
  :root{
    --page:#ecebe8;
    --card-white:#ffffff;
    --leaf:#8cc63f;
    --leaf-light:#a9d65a;
    --ocean:#2f6aa3;
    --ocean-deep:#285d91;
    --sky:#4a90c8;
    --ink:#1f2326;
    --grey:#6b6f73;
  }
  *{box-sizing:border-box;margin:0;padding:0}
  html,body{width:1200px;height:1023px;overflow:hidden}
  body{background:var(--page);font-family:"Open Sans",Arial,sans-serif;position:relative}

  .card{position:absolute;left:320px;width:560px;height:320px;border-radius:22px;overflow:hidden;
        box-shadow:0 6px 18px rgba(0,0,0,.18)}
  .card--front{top:110px;background:var(--card-white)}
  .card--back{top:592px;background:linear-gradient(160deg,var(--ocean) 0%,var(--ocean-deep) 100%)}

  .front-shape{position:absolute;inset:0;width:100%;height:100%}

  .contact{position:absolute;right:34px;top:30px;text-align:right;color:var(--ink)}
  .contact__name{font-size:24px;font-weight:600;color:var(--sky);line-height:1.1}
  .contact__role{font-size:17px;margin-top:2px}
  .contact__list{list-style:none;margin-top:22px}
  .contact__item{font-size:16px;line-height:1.55;display:flex;justify-content:flex-end;align-items:center;gap:10px}
  .contact__icon{width:14px;height:14px;flex:none}

  .brand{position:absolute;display:flex;align-items:center;gap:12px}
  .brand--front{left:30px;bottom:36px}
  .brand__dot{border-radius:50%;flex:none}
  .brand--front .brand__dot{width:32px;height:32px;background:var(--leaf)}
  .brand__text{display:flex;flex-direction:column;white-space:nowrap}
  .brand__name{font-weight:700;line-height:1}
  .brand--front .brand__name{font-size:18px;color:var(--ink)}
  .brand__rule{height:1px;margin:6px 0 5px}
  .brand--front .brand__rule{background:var(--grey)}
  .brand__tagline{text-transform:uppercase;letter-spacing:.04em}
  .brand--front .brand__tagline{font-size:7px;color:var(--grey);line-height:1.4}

  .brand--back{left:50%;top:50%;transform:translate(-50%,-50%);gap:22px}
  .brand--back .brand__dot{width:72px;height:72px;background:var(--leaf)}
  .brand--back .brand__name{font-size:34px;color:#fff}
  .brand--back .brand__rule{background:#fff;margin:10px 0 8px}
  .brand--back .brand__tagline{font-size:11px;color:#fff;line-height:1.4}
</style>
</head>
<body>

<section class="card card--front" aria-label="Business card front">
  <svg class="front-shape" viewBox="0 0 560 320" preserveAspectRatio="none" aria-hidden="true">
    <defs>
      <linearGradient id="leafFill" x1="0" y1="0" x2="1" y2="1">
        <stop offset="0" stop-color="#a9d65a"/>
        <stop offset="1" stop-color="#7dbb33"/>
      </linearGradient>
    </defs>
    <path d="M0 0 H560 V320 H458 C368 238 195 183 0 178 Z" fill="#4a90c8"/>
    <path d="M0 0 H560 V320 H470 C380 230 200 175 0 168 Z" fill="url(#leafFill)"/>
  </svg>

  <div class="contact">
    <p class="contact__name">Peter Odell</p>
    <p class="contact__role">Managing Director</p>
    <ul class="contact__list">
      <li class="contact__item">+1.628.307.4190
        <svg class="contact__icon" viewBox="0 0 16 16"><circle cx="8" cy="8" r="8" fill="#4a90c8"/><path d="M5 4.5h2l.7 2-1 .8a5 5 0 0 0 2 2l.8-1 2 .7v2c-4 .3-7-2.7-6.5-6.5z" fill="#fff"/></svg>
      </li>
      <li class="contact__item">peter@theharborlinegroup.com
        <svg class="contact__icon" viewBox="0 0 16 16"><circle cx="8" cy="8" r="8" fill="#4a90c8"/><rect x="4" y="5.2" width="8" height="5.6" fill="#fff"/><path d="M4 5.2l4 3 4-3" fill="none" stroke="#4a90c8" stroke-width=".9"/></svg>
      </li>
      <li class="contact__item">www.theharborlinegroup.com
        <svg class="contact__icon" viewBox="0 0 16 16"><circle cx="8" cy="8" r="8" fill="#4a90c8"/><circle cx="8" cy="8" r="4.3" fill="none" stroke="#fff" stroke-width="1"/><path d="M3.7 8h8.6M8 3.7c-2 2.5-2 6.1 0 8.6M8 3.7c2 2.5 2 6.1 0 8.6" fill="none" stroke="#fff" stroke-width=".9"/></svg>
      </li>
    </ul>
  </div>

  <div class="brand brand--front">
    <span class="brand__dot"></span>
    <div class="brand__text">
      <span class="brand__name">The Harborline Group</span>
      <span class="brand__rule"></span>
      <span class="brand__tagline">Venture fund and innovation accelerator<br>for exponential technologies</span>
    </div>
  </div>
</section>

<section class="card card--back" aria-label="Business card back">
  <div class="brand brand--back">
    <span class="brand__dot"></span>
    <div class="brand__text">
      <span class="brand__name">The Harborline Group</span>
      <span class="brand__rule"></span>
      <span class="brand__tagline">Venture fund and innovation accelerator<br>for exponential technologies</span>
    </div>
  </div>
</section>

</body>
</html>
```